Plakat-Design für Wartezimmer von Zahnarztpraxen
Zielgruppe
Wir sind ein Zahnärztlicher Berufsverband. Das Poster soll an unsere Mitglieder verteilt werden, so dass es in Wartezimmern von Zahnarztpraxen hängen wird.
Aufgabenstellung
Wir wollen einen Eyecatcher fürs Wartezimmer im Din A 1-Format.
Das Design soll im Pop-Art-Stil sein. Bitte den Entwurf im Anhang beachten. Dies beschreibt das gewünschte Poster schon sehr gut, allerdings ist es noch deutlich verbesserbar :-)
Idee : Maske ab, Mund auf (soll provozieren) und über den Stern das 'Kleingedruckte' die Message an die Patienten weitergeben:
Nur zur Behandlung bei Ihrem Zahnarzt. Trotz Pandemie immer für Sie da! Denn gesund beginnt im Mund.
Der Mund aus dem Entwurf gefällt uns sehr gut und kommt von der Google-Bildersuche. (ist allerdings zu erwerben)
Evtl. Die Farben anpassen an die Farben unseres Verbandes: www.bkpo.de
das Dokument unseres Verbandes gebe ich dazu, es muss allerdings ergänzt werden um: Landesverband RT

```html
<!DOCTYPE html>
<html lang="de">
<head>
<meta charset="utf-8">
<title>Maske ab – Mund auf</title>
<link href="https://fonts.googleapis.com/css2?family=Bangers&family=Delius&family=Montserrat:wght@500;800&display=swap" rel="stylesheet">
<style>
  :root {
    --cream: #f0ead6;
    --sky: #66b9ec;
    --navy: #0b3c66;
    --yellow: #ffd21a;
    --amber: #fbb814;
    --lip-red: #e3102c;
    --olive: #7d7658;
  }
  html, body { margin: 0; padding: 0; overflow: hidden; }
  body { width: 908px; height: 1200px; background: var(--cream); }
  .poster { position: relative; width: 908px; height: 1200px; background: var(--cream); overflow: hidden; }
  .sky-panel { position: absolute; left: 28px; top: 25px; width: 852px; height: 957px; background: var(--sky); overflow: hidden; }
  .rays { position: absolute; inset: 0; }
  .mouth-art {
    position: absolute; left: 170px; top: 104px; width: 500px; height: 700px;
    border-radius: 50% / 48%;
    background: radial-gradient(ellipse at 50% 50%, var(--navy) 0%, var(--navy) 40%, #6a2446 70%, var(--lip-red) 92%);
    box-shadow: 0 24px 30px -18px rgba(11,60,102,.35);
  }
  .headline {
    position: absolute; left: 0; top: 0; width: 908px; height: 700px; margin: 0;
    font-family: "Bangers", "Impact", sans-serif; font-weight: 400;
    transform: rotate(-6deg);
    transform-origin: 470px 450px;
  }
  .headline span {
    position: absolute; display: block; white-space: nowrap; line-height: 1;
    background: linear-gradient(90deg, #fff200, var(--yellow) 50%, var(--amber));
    -webkit-background-clip: text; background-clip: text; color: transparent;
    -webkit-text-stroke: 3px var(--navy);
    filter: drop-shadow(-7px 6px 0 var(--navy));
  }
  .headline .line-one { left: 135px; top: 285px; font-size: 198px; letter-spacing: 2px; }
  .headline .line-two { left: 160px; top: 452px; font-size: 166px; letter-spacing: 1px; }
  .asterisk-mark { position: absolute; left: 750px; top: 450px; width: 48px; height: 48px; z-index: 3; }
  .fine-print {
    position: absolute; left: 68px; top: 952px; width: 446px; height: 146px; margin: 0;
    background: linear-gradient(90deg, var(--yellow), #ffcc12);
    border: 3px solid var(--navy);
    box-shadow: 5px 6px 0 var(--navy);
    box-sizing: border-box; padding: 12px 10px 0 30px;
    font-family: "Delius", "Comic Sans MS", cursive; font-size: 24px; line-height: 28px; letter-spacing: 1.2px; color: var(--navy);
    white-space: nowrap;
  }
  .fine-print-star { position: absolute; left: 48px; top: 938px; width: 40px; height: 40px; z-index: 3; }
  .web-address { position: absolute; left: 70px; top: 1124px; font-family: "Montserrat", sans-serif; font-weight: 500; font-size: 19px; letter-spacing: 1.6px; color: var(--navy); }
  .chapter { position: absolute; right: 47px; top: 1124px; font-family: "Montserrat", sans-serif; font-weight: 500; font-size: 19px; letter-spacing: 1.6px; color: var(--navy); }
  .association { position: absolute; left: 599px; top: 1028px; display: flex; align-items: center; gap: 18px; }
  .association-square { width: 50px; height: 72px; border: 2px solid var(--olive); box-sizing: border-box; }
  .association-name { font-family: "Montserrat", sans-serif; font-weight: 800; font-size: 21px; line-height: 27px; letter-spacing: .5px; color: var(--olive); margin: 0; }
</style>
</head>
<body>
<div class="poster">
  <div class="sky-panel">
    <svg class="rays" width="852" height="957" viewBox="0 0 852 957" aria-hidden="true">
      <g fill="var(--cream)">
        <polygon points="0,27 0,40 190,172"/>
        <polygon points="327,0 342,0 373,88"/>
        <polygon points="399,0 407,0 408,112"/>
        <polygon points="852,26 852,40 680,130"/>
        <polygon points="0,305 0,318 140,333"/>
        <polygon points="0,410 0,422 120,410"/>
        <polygon points="0,625 0,640 80,605"/>
        <polygon points="852,270 852,282 785,294"/>
        <polygon points="852,467 852,477 725,491"/>
        <polygon points="852,565 852,576 715,575"/>
        <polygon points="852,765 852,780 662,673"/>
        <polygon points="852,895 852,910 715,792"/>
        <polygon points="0,855 0,872 185,773"/>
        <polygon points="184,905 192,910 225,828"/>
        <polygon points="426,957 437,957 434,890"/>
      </g>
      <g fill="var(--navy)">
        <polygon points="660,118 665,121 600,200 597,197"/>
        <polygon points="150,312 154,307 235,345 231,349"/>
        <polygon points="220,705 217,700 260,675 263,680"/>
        <polygon points="700,722 697,727 765,755 768,750"/>
      </g>
    </svg>
    <div class="mouth-art" role="img" aria-label="Pop-Art-Illustration eines weit geöffneten Mundes mit roten Lippen und weißen Zähnen"></div>
  </div>

  <h1 class="headline">
    <span class="line-one">MASKE AB</span>
    <span class="line-two">MUND AUF</span>
  </h1>
  <svg class="asterisk-mark" viewBox="-24 -24 48 48" aria-hidden="true">
    <g stroke="var(--navy)" stroke-width="10" stroke-linecap="butt">
      <line x1="0" y1="-22" x2="0" y2="22"/>
      <line x1="-19" y1="-11" x2="19" y2="11"/>
      <line x1="-19" y1="11" x2="19" y2="-11"/>
    </g>
  </svg>

  <p class="fine-print">Nur zur Behandlung bei Ihrem<br>Zahnarzt. Trotz Pandemie<br>immer für Sie da! Denn<br>gesund beginnt im Mund.</p>
  <svg class="fine-print-star" viewBox="-24 -24 48 48" aria-hidden="true">
    <g stroke-linecap="round">
      <g stroke="var(--navy)" stroke-width="14">
        <line x1="0" y1="-18" x2="0" y2="18"/>
        <line x1="-16" y1="-9" x2="16" y2="9"/>
        <line x1="-16" y1="9" x2="16" y2="-9"/>
      </g>
      <g stroke="#fff" stroke-width="8">
        <line x1="0" y1="-18" x2="0" y2="18"/>
        <line x1="-16" y1="-9" x2="16" y2="9"/>
        <line x1="-16" y1="9" x2="16" y2="-9"/>
      </g>
    </g>
  </svg>

  <div class="association">
    <div class="association-square"></div>
    <p class="association-name">Bund<br>Kieferpraxen<br>Ost e.V.</p>
  </div>

  <div class="web-address">www.bkpo.de</div>
  <div class="chapter">Landesverband RT</div>
</div>
</body>
</html>
```